Stationary design for a bidet toilet seat
Vellora Bidets
Stationary design for a bidet toilet seat  - Health
Creative Brief
Bright & Fun-filled
Tobias Merrick III
Marketing Agent
418 Westmere Ave. Suite 203 Corvale, NV 89012
vellorabidets@quillpost-mail.com
My logo was done by Quorvan designs

```html
<!DOCTYPE html>
<html lang="en">
<head>
<meta charset="utf-8">
<title>Vellora Bidets – Business Card</title>
<link href="https://fonts.googleapis.com/css2?family=Libre+Baskerville:wght@400;700&display=swap" rel="stylesheet">
<style>
  :root {
    --bg: #8a8a8a;
    --blue: #2f86cc;
    --blue-light: #4aa3e0;
    --blue-dark: #1f6fb3;
    --green: #5aa832;
    --white: #ffffff;
    --ink: #2b2b2b;
    --muted: #5a5a5a;
    --serif: "Libre Baskerville", "Times New Roman", serif;
  }
  html, body {
    margin: 0; padding: 0;
    width: 1200px; height: 908px;
    overflow: hidden;
    background: var(--bg);
    font-family: var(--serif);
  }
  .stage {
    position: relative;
    width: 1200px; height: 908px;
  }
  .card {
    position: absolute;
    top: 300px;
    width: 540px; height: 309px;
    border-radius: 22px;
    overflow: hidden;
    box-shadow: 0 8px 20px rgba(0,0,0,.25);
  }
  /* Front */
  .card-front {
    left: 45px;
    background: linear-gradient(135deg, var(--blue-light) 0%, var(--blue) 55%, var(--blue-dark) 100%);
  }
  .front-ring {
    position: absolute;
    left: -40px; top: 70px;
    width: 260px; height: 260px;
    border-radius: 50%;
    background: rgba(140, 200, 190, .35);
  }
  .front-brand {
    position: absolute;
    right: 40px; top: 116px;
    color: var(--white);
    font-size: 20px;
    letter-spacing: 2px;
    text-transform: uppercase;
    white-space: nowrap;
  }
  /* Back */
  .card-back {
    left: 615px;
    background: var(--white);
  }
  .back-wave {
    position: absolute; inset: 0;
    width: 540px; height: 309px;
  }
  .back-brand {
    position: absolute;
    left: 250px; top: 134px;
    display: flex; align-items: center; gap: 10px;
    color: var(--blue);
    font-size: 18px;
    letter-spacing: 2px;
    text-transform: uppercase;
    white-space: nowrap;
  }
  .brand-dot {
    width: 24px; height: 24px;
    border-radius: 50%;
    background: var(--green);
  }
  .person {
    position: absolute;
    right: 36px; top: 192px;
    text-align: right;
  }
  .person-name {
    margin: 0;
    color: var(--green);
    font-size: 15px;
    letter-spacing: 1px;
    text-transform: uppercase;
    font-weight: 400;
    white-space: nowrap;
  }
  .person-role {
    margin: 4px 0 0;
    color: var(--muted);
    font-size: 9px;
    letter-spacing: 1.5px;
    text-transform: uppercase;
  }
  .contact {
    position: absolute;
    left: 26px; bottom: 22px;
    color: var(--ink);
    font-size: 9.5px;
    line-height: 1.5;
  }
  .contact p { margin: 0; }
  .contact .line { display: flex; align-items: center; gap: 5px; }
  .contact svg { width: 10px; height: 10px; flex: none; }
</style>
</head>
<body>
<main class="stage">

  <section class="card card-front" aria-label="Card front">
    <div class="front-ring"></div>
    <div class="front-brand">Vellora Bidets</div>
  </section>

  <section class="card card-back" aria-label="Card back">
    <svg class="back-wave" viewBox="0 0 540 309" preserveAspectRatio="none">
      <path d="M0 0 H540 V18 C420 34 320 60 230 100 C150 136 70 158 0 164 Z" fill="var(--blue)"/>
      <path d="M540 18 C420 34 320 60 230 100 C150 136 70 158 0 164 L0 172 C72 166 154 144 236 108 C326 70 424 42 540 28 Z" fill="var(--green)"/>
    </svg>

    <div class="back-brand"><span class="brand-dot"></span>Vellora Bidets</div>

    <div class="person">
      <h2 class="person-name">Tobias Merrick III</h2>
      <p class="person-role">Marketing Agent</p>
    </div>

    <div class="contact">
      <p>418 Westmere Ave.</p>
      <p>Suite 203</p>
      <p>Corvale, NV 89012</p>
      <p class="line">
        <svg viewBox="0 0 10 10"><circle cx="5" cy="5" r="5" fill="var(--green)"/><path d="M3 2.5 l1 0 .5 1.4 -.6.5 a4 4 0 0 0 1.7 1.7 l.5-.6 1.4.5 0 1 a4.5 4.5 0 0 1-4.5-4.5z" fill="#fff"/></svg>
        555-201-4730
      </p>
      <p class="line">
        <svg viewBox="0 0 10 10"><circle cx="5" cy="5" r="5" fill="var(--green)"/><path d="M3 2.5 l1 0 .5 1.4 -.6.5 a4 4 0 0 0 1.7 1.7 l.5-.6 1.4.5 0 1 a4.5 4.5 0 0 1-4.5-4.5z" fill="#fff"/></svg>
        555-201-4731
      </p>
      <p class="line">
        <svg viewBox="0 0 10 10"><circle cx="5" cy="5" r="5" fill="var(--green)"/><rect x="2.4" y="3.2" width="5.2" height="3.6" fill="#fff"/><path d="M2.4 3.2 L5 5.2 L7.6 3.2" stroke="var(--green)" stroke-width=".6" fill="none"/></svg>
        vellorabidets@quillpost-mail.com
      </p>
    </div>
  </section>

</main>
</body>
</html>
```